Clean, Corporate redesign of existing website

We require a clean corporate professional redesign of our existing poor website, although a simple and elegant structure is required we would like the designer to concentrate on the little things and finishes to give the site a highly professional feel.
The company have supplied the following websites as to use as inspiration http://www.dorvalestone.example/ they like the clean, professional feel of the website
and the fact that the website captures the feel of their industry. Another clean and professional site they liked the look of was http://www.brisklyseafare.example.co.uk/ .
Another inspirational (page level only) http://www.halvertonexpohall.example/thefacilities/floor-maps-and-specifications/ we like the top image and the corporate feel the images give. Auto cad drawings as images or a search for electrical services will fetch up a good selection of images to use as placeholders
A full brief, logos, images etc have been supplied
update: the sector is industrial electrical services, so more towards factory switches and equipement, not domestic light-bulbs etc this is important when choosing images for the site.
Updates
Thank you all for your designs, i will be presenting the best to the company tomorrow who will pick the design that suits so please get any remaining designs to me by tomorrow morning (GMT time) at the latest to be included in the presentation.
Target Market(s)
Business owners and CEO'S
Industry/Entity Type
Electrical
Look and feel

```html
<!DOCTYPE html>
<html lang="en">
<head>
<meta charset="utf-8">
<title>Wold Electrical Services Limited</title>
<link rel="stylesheet" href="https://fonts.googleapis.com/css2?family=League+Gothic&display=swap">
<style>
:root{
  --orange:#ea3c05;
  --dark:#231f1c;
  --text:#3a3a3a;
  --grey:#e8e8e8;
  --line:#9a9a9a;
  --white:#ffffff;
  --display:"League Gothic",sans-serif;
}
*{box-sizing:border-box;margin:0;padding:0}
html,body{width:811px;height:1200px;overflow:hidden;background:var(--white)}
.page{position:relative;width:811px;height:1200px;overflow:hidden;font-family:Arial,Helvetica,sans-serif;color:var(--text);
  background:linear-gradient(90deg,transparent 0 40px,rgba(0,0,0,.03) 40px 90px,transparent 90px 325px,rgba(0,0,0,.035) 325px 465px,transparent 465px 600px,rgba(0,0,0,.03) 600px 680px,transparent 680px),var(--white)}
.edge{position:absolute;left:0;width:811px;height:10px}
.edge-top{top:0;background:
  linear-gradient(135deg,var(--orange) 50%,transparent 50%) 0 0/10px 10px repeat-x,
  linear-gradient(225deg,var(--orange) 50%,transparent 50%) 0 0/10px 10px repeat-x}
.edge-top{background:linear-gradient(to bottom right,var(--orange) 50%,transparent 50%) 0 0/5px 10px repeat-x,linear-gradient(to bottom left,var(--orange) 50%,transparent 50%) 5px 0/10px 10px repeat-x}
.edge-bottom{bottom:0;background:linear-gradient(to top right,var(--orange) 50%,transparent 50%) 0 0/10px 10px repeat-x}
.logo{position:absolute;left:30px;top:44px;display:flex;align-items:center;gap:9px;font-family:var(--display);font-size:38px;line-height:1;color:var(--dark);letter-spacing:.3px}
.logo i{width:14px;height:14px;background:var(--orange)}
.callus{position:absolute;right:18px;top:30px;font-family:var(--display);font-size:21px;color:#666;letter-spacing:.3px}
.nav{position:absolute;left:346px;top:63px;width:465px;height:37px;background:var(--orange);display:flex;font-family:var(--display);font-size:18px;letter-spacing:.3px}
.nav a{color:var(--white);text-decoration:none;display:flex;align-items:center;justify-content:center}
.nav .active{background:var(--dark);width:60px}
.nav a:nth-child(2){width:85px}.nav a:nth-child(3){width:90px}.nav a:nth-child(4){width:125px}.nav a:nth-child(5){width:105px}
.hero-photo{position:absolute;left:0;top:125px;width:470px;height:350px;
  background:radial-gradient(ellipse at 45% 45%,#b9bdc2 0,#d9dbdd 35%,rgba(240,240,240,0) 70%)}
.headline{position:absolute;left:347px;top:262px;font-family:var(--display);line-height:1;white-space:nowrap}
.headline .lead{color:var(--orange);font-size:37px;letter-spacing:.2px}
.headline .main{color:var(--dark);font-size:54px;margin-top:2px;letter-spacing:.2px}
.arrows{position:absolute;left:682px;top:393px}
.clients-title{position:absolute;left:294px;top:458px;font-family:var(--display);font-size:31px;color:var(--orange);line-height:1}
.clients{position:absolute;left:295px;top:489px;width:479px;height:91px;background:#efefef;border:1px solid #d8d8d8;display:flex;align-items:center;justify-content:space-around;padding:0 6px}
.client{display:flex;align-items:center;gap:5px;font-family:var(--display);font-size:16px;color:var(--dark);text-align:center;line-height:1.05;letter-spacing:.3px}
.client i{width:10px;height:10px;border-radius:50%;background:var(--orange);flex:none}
.welcome{position:absolute;left:32px;top:660px;width:418px}
.welcome h1{font-family:var(--display);font-weight:400;font-size:29px;line-height:1;color:var(--orange);margin-bottom:7px}
.welcome p{font-size:12.7px;line-height:18.6px;text-align:justify;margin-bottom:18.6px;padding-left:2px}
.gallery{position:absolute;left:469px;top:638px;width:292px;height:244px}
.intro{position:absolute;left:482px;top:913px;width:300px;font-size:12px;line-height:18px}
.sectors{position:absolute;left:471px;top:960px;width:313px;height:79px;background:var(--orange);display:grid;grid-template-columns:141px 172px;align-content:center;padding-left:7px;row-gap:12px;font-family:var(--display);font-size:21px;color:var(--white);letter-spacing:.2px}
.sectors li{list-style:none;display:flex;align-items:center;gap:7px;line-height:1}
.sectors li::before{content:"";width:6px;height:6px;background:var(--white)}
.extra{position:absolute;left:471px;top:1039px;width:313px;height:106px;background:var(--grey);border-bottom:4px solid var(--line);padding:12px 12px 0 12px;font-size:12px;line-height:17px;text-align:justify}
.extra p+p{margin-top:17px}
.footer{position:absolute;left:35px;top:1158px;width:419px;height:42px;background:var(--orange);border-radius:7px 7px 0 0;color:var(--white);font-family:var(--display);font-size:17px;display:flex;align-items:center;justify-content:center;letter-spacing:.2px;z-index:2}
</style>
</head>
<body>
<div class="page">
  <div class="edge edge-top"></div>

  <div class="hero-photo" role="img" aria-label="Close-up photo of a hand turning a rotary switch on an industrial control panel"></div>

  <div class="logo"><i></i>Wold Electrical Services</div>
  <div class="callus">CALL US NOW : 000-0000-000</div>

  <nav class="nav">
    <a class="active" href="#">HOME</a>
    <a href="#">SERVICES</a>
    <a href="#">CLIENTS</a>
    <a href="#">HEALTH &amp; SAFETY</a>
    <a href="#">CONTACT US</a>
  </nav>

  <div class="headline">
    <div class="lead">COMMERCIAL . INDUSTRIAL . DOMESTIC</div>
    <div class="main">ELECTRICAL INSTALLATIONS</div>
  </div>

  <svg class="arrows" width="68" height="48" viewBox="0 0 68 48" aria-label="Previous and next slide">
    <path d="M24 2 L8 24 L24 46 L16 46 L0 24 L16 2 Z" fill="var(--dark)"/>
    <path d="M44 2 L60 24 L44 46 L52 46 L68 24 L52 2 Z" fill="var(--dark)"/>
  </svg>

  <div class="clients-title">OUR CLIENTS</div>
  <div class="clients">
    <div class="client"><i></i>Ridgeway<br>Motors</div>
    <div class="client"><i></i>Alpine<br>Kite</div>
    <div class="client"><i></i>Norvik<br>Auto</div>
    <div class="client"><i></i>Brightwell<br>Drinks</div>
    <div class="client"><i></i>Hoopline<br>League</div>
    <div class="client"><i></i>Meridian<br>Systems</div>
  </div>

  <section class="welcome">
    <h1>WELCOME TO DORVALE STONE PLC</h1>
    <p>Established in 2005 Wold Electrical Services Limited is an independent company that has grown steadily over that period into a respected Commercial and Domestic Electrical installer providing it’s services nationwide.</p>
    <p>Professional and reliable, the secret of our success has come from recommendations from our customer base. Our staffing levels allow us to be flexible enough to tackle any size of project, contracts often exceeding 100K, yet we are able to complete the more modest budget competitively. All our work is guaranteed and our help line is always available to our clients to satisfy any after contract queries or concerns.</p>
    <p>As a company we strive to meet exceptional standards of workmanship, we are registered with the National Register for Electrical Installation Standards and all our work is certificated accordingly. All our engineers are fully qualified in their relevant fields and all work there is carried out to BS 7671 standards.</p>
    <p>As Health and safety is always such a major factor in the industry, we always ensure that at least one qualified representative is present on each site. We also employ the services of health and safety consultants on a permanent basis.</p>
  </section>

  <svg class="gallery" viewBox="0 0 292 244" role="img" aria-label="Two circular photos of industrial switchgear panels with indicator lights">
    <defs>
      <linearGradient id="panel" x1="0" y1="0" x2="1" y2="1">
        <stop offset="0" stop-color="#6f7378"/>
        <stop offset=".5" stop-color="#c9cccf"/>
        <stop offset="1" stop-color="#e9eaeb"/>
      </linearGradient>
    </defs>
    <circle cx="115" cy="114" r="114" fill="#e6e6e6"/>
    <circle cx="115" cy="114" r="106" fill="url(#panel)"/>
    <ellipse cx="247" cy="157" rx="44" ry="79" fill="#e6e6e6"/>
    <ellipse cx="249" cy="157" rx="38" ry="71" fill="url(#panel)"/>
  </svg>

  <p class="intro">The Company is extensively experienced throughout a broad spectrum of electrical projects, which encompass:</p>
  <ul class="sectors">
    <li>FOOD INDUSTRY</li>
    <li>RETAIL PREMISES</li>
    <li>COUNCILS</li>
    <li>SCHOOLS AND COLLEGES</li>
  </ul>
  <div class="extra">
    <p>Further more we carryout system testing, faultfinding and survey reports.</p>
    <p>We also specialise in fire alarm inspection and testing reports.</p>
  </div>

  <footer class="footer">PHONE: 01632 960600 | FAX: 01632 960510 | EMAIL: INFO@WOLDELECTRICAL.EXAMPLE</footer>
  <div class="edge edge-bottom"></div>
</div>
</body>
</html>
```